Business Card Design

I would like a double sided business card design.

1 side showing usual contact details and small version of logo (attached "LarkVeil")

other side with larger logo and artwork with room to list what we specialise in.

Lark Veil is a Fashion Millinery Design and Sales Business.

I have attached some other examples of te styles i like so you can see what sort of taste i have.

Feel free to play around with colours of logo - it is grey as i originall had in mind a black background with monochrome silver logo.
Updates

• Please send me a message with your quote after posting your design. Budget set at Minimum (FYI) and negotiable
• Supporting files are examples only - i do not wish to copy them.  The only file for exact use is my logo "LarkVeil"
• Thank you

Target Market(s)

18 - 80 yo females mainly

Industry/Entity Type

Business

Requirements
Must have
• unique and striking individuality
Should not have
• boring and normal

```html
<!DOCTYPE html>
<html lang="en">
<head>
<meta charset="utf-8">
<title>LarkVeil — Business Cards</title>
<link rel="stylesheet" href="https://fonts.googleapis.com/css2?family=Roboto+Condensed:wght@300;400;700&display=swap">
<style>
  :root {
    --page-bg: #ffffff;
    --card-light: #ededee;
    --card-dark: #211d1b;
    --logo-white: #ffffff;
    --silver: #8a8a8c;
    --text-grey: #6d6e71;
    --ink: #1a1a1a;
    --blush: #efc3d7;
    --blush-deep: #eab4cd;
    --blush-clear: rgba(239, 195, 215, 0);
  }
  * { box-sizing: border-box; margin: 0; padding: 0; }
  html, body {
    width: 1200px;
    height: 638px;
    overflow: hidden;
    background: var(--page-bg);
  }
  body {
    position: relative;
    font-family: "Roboto Condensed", "Arial Narrow", sans-serif;
  }
  .card {
    position: absolute;
    top: 180px;
    width: 464px;
    height: 277px;
    background: var(--card-light);
    overflow: hidden;
    box-shadow: 0 1px 4px rgba(0, 0, 0, 0.15);
  }
  .card--front { left: 119px; }
  .card--back { left: 618px; }

  /* Front */
  .front__dark-panel {
    position: absolute;
    left: 0; top: 0;
    width: 238px; height: 100%;
    background: var(--card-dark);
  }
  .front__artwork {
    position: absolute;
    left: 238px; top: 0;
    width: 226px; height: 100%;
    background:
      radial-gradient(circle at 48% 30%, var(--blush-deep) 0%, var(--blush-deep) 14%, var(--blush) 26%, var(--blush-clear) 48%),
      radial-gradient(circle at 74% 88%, var(--blush-deep) 0%, var(--blush) 16%, var(--blush-clear) 34%),
      radial-gradient(circle at 36% 86%, var(--blush) 0%, var(--blush-clear) 26%),
      radial-gradient(ellipse at 60% 62%, rgba(239,195,215,0.7) 0%, var(--blush-clear) 55%),
      var(--card-light);
  }
  .front__name {
    position: absolute;
    left: 0; width: 238px;
    top: 94px;
    text-align: center;
    font-weight: 300;
    font-size: 60px;
    line-height: 1;
    letter-spacing: 0.5px;
    color: var(--logo-white);
  }

  /* Back */
  .back__artwork {
    position: absolute;
    left: 0; top: 0;
    width: 150px; height: 100%;
    background:
      radial-gradient(ellipse at 8% 26%, var(--blush-deep) 0%, var(--blush) 22%, var(--blush-clear) 52%),
      radial-gradient(circle at 30% 90%, var(--blush) 0%, rgba(239,195,215,0.5) 22%, var(--blush-clear) 45%),
      radial-gradient(ellipse at 50% 60%, rgba(239,195,215,0.5) 0%, var(--blush-clear) 55%);
  }
  .back__name {
    position: absolute;
    left: 125px; width: 210px;
    top: 78px;
    text-align: center;
    font-weight: 300;
    font-size: 56px;
    line-height: 1;
    color: var(--silver);
  }
  .back__contact {
    position: absolute;
    left: 125px; width: 210px;
    top: 139px;
    text-align: center;
    font-size: 13.5px;
    line-height: 16.3px;
    color: var(--text-grey);
  }
  .back__contact b { font-weight: 700; }
  .back__staff {
    position: absolute;
    left: 0; top: 249px;
    width: 100%;
    height: 26px;
  }
  .staff__field {
    position: absolute;
    top: 0;
    height: 26px;
    border-left: 1px solid var(--ink);
    padding-left: 5px;
    font-size: 13.5px;
    line-height: 14px;
    color: var(--ink);
  }
  .staff__field--name { left: 16px; }
  .staff__field--cell { left: 122px; }
  .staff__field--email { left: 232px; }
</style>
</head>
<body>
  <section class="card card--front">
    <div class="front__dark-panel"></div>
    <div class="front__artwork" role="img" aria-label="Pink swirling floral ornament artwork with circles and tendrils"></div>
    <div class="front__name">LarkVeil</div>
  </section>

  <section class="card card--back">
    <div class="back__artwork" role="img" aria-label="Faded pink swirling floral ornament artwork"></div>
    <div class="back__name">LarkVeil</div>
    <div class="back__contact">
      <p>Abcd, efghijklmnopqrst, vwxyz</p>
      <p><b>Ph:</b> 91+00000000000, 000000</p>
      <p><b>Email:</b> hello@larkveil.com</p>
      <p><b>Website:</b> www.larkveil.com</p>
    </div>
    <div class="back__staff">
      <span class="staff__field staff__field--name">director Name</span>
      <span class="staff__field staff__field--cell">cell</span>
      <span class="staff__field staff__field--email">email</span>
    </div>
  </section>
</body>
</html>
```